Flyer-Design für nachhaltige Spülbecher aus Keramik
Zielgruppe
Zielgruppe des Flyers sind Zahnärzte. Wir fertigen die ersten nachhaltigen Spülbecher für Praxen aus Keramik.
Aufgabenstellung
Der Flyer soll einen hochwertigen und exklusiven Eindruck hinterlassen.
Auf dem Flyer sollte das Logo, Kontaktmöglichkeiten, Anschrift, 1-2 Bilder des Produktes und ein kleiner Text bezüglich Nachhaltigkeit vorhanden sein. Die aktuell hochgeladenen Bilder der Becher sind aktuell noch Platzhalter, es werden in den nächsten Tagen die richtigen Bilder hochgeladen.
WICHTIG: Bitte einen Platzhalter für eine Überschrift und Stichpunkte/Informationen einarbeiten. Leider ist noch nicht Final klar wir diese Lauten soll, daher wird dieser Teil noch von mir noch selbst ergänzt. Danke
Website: www.lindgau-keramik.de

```html
<!DOCTYPE html>
<html lang="de">
<head>
<meta charset="utf-8">
<title>Lindgau Keramik – Flyer Spülbecher</title>
<link href="https://fonts.googleapis.com/css2?family=Libre+Baskerville:wght@400;700&family=Open+Sans:wght@400;600;700&display=swap" rel="stylesheet">
<style>
  :root {
    --stage: #e6e6e4;
    --paper: #ffffff;
    --ink: #1e1e1e;
    --muted: #8a8a8a;
    --shadow: rgba(0,0,0,.18);
    --serif: "Libre Baskerville", Georgia, serif;
    --sans: "Open Sans", Arial, sans-serif;
  }
  * { box-sizing: border-box; margin: 0; padding: 0; }
  html, body { width: 1200px; height: 625px; overflow: hidden; }
  body { background: var(--stage); font-family: var(--sans); color: var(--ink); }

  .sheet {
    position: absolute; top: 52px; width: 520px; height: 520px;
    background: var(--paper); box-shadow: 0 3px 10px var(--shadow);
    display: flex;
  }
  .sheet--front { left: 60px; }
  .sheet--back { left: 620px; }

  .text-column { position: relative; width: 186px; height: 100%; }
  .photo { position: relative; flex: 1; height: 100%; overflow: hidden; }

  .brand-mark { position: absolute; top: 32px; left: 34px; display: flex; align-items: center; gap: 7px; }
  .brand-mark__square { width: 16px; height: 16px; border: 1.5px solid var(--ink); }
  .brand-mark__name { font-size: 9px; font-weight: 600; }

  .headline { position: absolute; top: 176px; left: 34px; font-family: var(--serif); font-size: 18px; line-height: 21px; font-weight: 400; }
  .headline__product { display: block; font-weight: 700; font-size: 21px; line-height: 27px; letter-spacing: .5px; }
  .headline__topic { display: block; text-transform: uppercase; letter-spacing: .3px; }

  .intro { position: absolute; top: 316px; left: 34px; width: 126px; font-size: 9.4px; line-height: 1.34; }

  .signature { position: absolute; bottom: 30px; left: 34px; }
  .signature__name { font-size: 10.5px; font-weight: 700; }
  .signature__claim { font-size: 6.5px; margin-top: 2px; }
  .sheet--back .signature { left: 0; right: 0; text-align: center; bottom: 26px; }
  .sheet--back .signature .brand-mark__square { display: block; margin: 0 auto 6px; }

  .contact { position: absolute; top: 78px; right: 24px; text-align: right; font-size: 9.6px; line-height: 1.36; color: var(--muted); font-style: normal; }
  .contact__company { color: var(--ink); font-weight: 600; }
  .contact__gap { height: 13px; }

  .photo--cup {
    background: linear-gradient(165deg, #eceef0 0%, #d9dde1 45%, #b9cad6 70%, #e4e5e6 100%);
  }
  .photo--range {
    background: linear-gradient(160deg, #2a2a2a 0%, #1a1a1a 55%, #111 100%);
  }

  .vertical-label { position: absolute; writing-mode: vertical-rl; }
  .vertical-label--product { right: 8px; bottom: 14px; font-size: 9px; color: var(--ink); }
  .vertical-label--web { right: 12px; top: 92px; font-family: var(--serif); font-size: 27px; color: #fff; letter-spacing: .3px; }
</style>
</head>
<body>

<section class="sheet sheet--front" aria-label="Flyer Vorderseite">
  <div class="text-column">
    <div class="brand-mark">
      <span class="brand-mark__square"></span>
      <span class="brand-mark__name">Lindgau Keramik</span>
    </div>
    <h1 class="headline">
      <span class="headline__product">-ONA-</span>
      <span class="headline__topic">Nach-</span>
      <span class="headline__topic">haltig-</span>
      <span class="headline__topic">keit</span>
    </h1>
    <p class="intro">Itatios ipit at. Osaniente magnatur? Ruptate ssi-maio moluptatur? Solut quos apis autest, net fu-giatatem volo ipsam que corum fugiatur? Qui non-</p>
    <div class="signature">
      <div class="signature__name">Lindgau Keramik</div>
      <div class="signature__claim">Wir brennen für Keramik.</div>
    </div>
  </div>
  <div class="photo photo--cup" role="img" aria-label="Produktfoto: blauer Keramik-Spülbecher unter einem weißen Mundspülauslauf">
    <span class="vertical-label vertical-label--product">Produktname</span>
  </div>
</section>

<section class="sheet sheet--back" aria-label="Flyer Rückseite">
  <div class="text-column">
    <address class="contact">
      <div class="contact__company">Lindgau Keramik GmbH</div>
      <div>Auenweg 8</div>
      <div>98631 Lindgau</div>
      <div class="contact__gap"></div>
      <div>info@lindgau-keramik.de</div>
      <div>0176 / 20481736</div>
    </address>
    <div class="signature">
      <span class="brand-mark__square"></span>
      <div class="signature__name">Lindgau Keramik</div>
      <div class="signature__claim">Wir brennen für Keramik.</div>
    </div>
  </div>
  <div class="photo photo--range" role="img" aria-label="Produktfoto: Keramikbecher in Rosé, Hellblau, Blau, Weiß, Grün und Grau auf dunklem Grund">
    <span class="vertical-label vertical-label--web">www.lindgau-keramik.de</span>
  </div>
</section>

</body>
</html>
```